Velorine Jewellery Display Card

We are a jewellery manufacturer and need artwork for an A4 size strut card to advertise our new "Crescent Loop Pendant "
In the attached files is a picture of the new pendant and artwork for our trademark "Velorine"
We also need to include the phrase " an expression of love "
as part of the artwork.
The background colour should be predominately white

Target Market(s)

This product has been designed as a gift for Mothers as it has their children names
engraved on the pendant

Industry/Entity Type

Manufacturer

Font styles to use
Serif
Script

Colors
ffffff

Requirements
Must have
• Artwork should be simple and elegant , the predominant look in Australian jewellery stores which is where these display cards will be is white, bright and elegant

```html
<!DOCTYPE html>
<html lang="en">
<head>
<meta charset="utf-8">
<title>Velorine – Crescent Loop Pendant Strut Card</title>
<link rel="stylesheet" href="https://fonts.googleapis.com/css2?family=Cormorant+Garamond:wght@400;500&family=Great+Vibes&display=swap">
<style>
  :root {
    --stage: #1b1b1b;
    --card: #ffffff;
    --ink-dark: #3a3a3a;
    --ink-mid: #6e6e6e;
    --ink-soft: #9a9a9a;
    --rule: #8c8c8c;
    --silver-light: #f2f2f2;
    --silver-mid: #c9c9c9;
    --silver-dark: #8f8f8f;
  }
  * { margin: 0; padding: 0; box-sizing: border-box; }
  html, body {
    width: 1200px;
    height: 750px;
    overflow: hidden;
    background: var(--stage);
  }
  .canvas {
    position: relative;
    width: 1200px;
    height: 750px;
  }
  .strut-card {
    position: absolute;
    left: 352px;
    top: 25px;
    width: 496px;
    height: 700px;
    background: var(--card);
    text-align: center;
    font-family: "Cormorant Garamond", Georgia, serif;
  }
  .product-title {
    position: absolute;
    left: 50%;
    top: 62px;
    transform: translateX(-50%);
    width: 250px;
  }
  .product-title__main {
    display: block;
    font-size: 40px;
    font-weight: 500;
    letter-spacing: 2px;
    color: var(--ink-dark);
    line-height: 44px;
    padding-bottom: 6px;
    border-bottom: 1.5px solid var(--rule);
  }
  .product-title__sub {
    display: block;
    font-size: 20px;
    font-weight: 500;
    letter-spacing: 4.5px;
    color: var(--ink-mid);
    line-height: 22px;
    padding: 9px 0 8px;
    border-bottom: 1.5px solid var(--rule);
  }
  .pendant-photo {
    position: absolute;
    left: 50%;
    top: 210px;
    transform: translateX(-50%);
    width: 170px;
    height: 240px;
  }
  .tagline {
    position: absolute;
    left: 0;
    right: 0;
    top: 492px;
    font-family: "Great Vibes", cursive;
    font-size: 38px;
    color: var(--ink-soft);
    line-height: 50px;
  }
  .occasion {
    position: absolute;
    left: 0;
    right: 0;
    top: 550px;
    font-size: 9.5px;
    font-weight: 500;
    letter-spacing: 0.4px;
    color: var(--ink-mid);
  }
  .brand-name {
    position: absolute;
    left: 0;
    right: 0;
    top: 604px;
    font-size: 26px;
    font-weight: 500;
    letter-spacing: 1.5px;
    color: var(--ink-soft);
  }
</style>
</head>
<body>
<main class="canvas">
  <article class="strut-card">
    <h1 class="product-title">
      <span class="product-title__main">CRESCENT</span>
      <span class="product-title__sub">LOOP PENDANT</span>
    </h1>

    <svg class="pendant-photo" viewBox="0 0 170 240" role="img" aria-label="Product photograph of the silver Crescent Loop Pendant with engraved children's names">
      <defs>
        <radialGradient id="silverTone" cx="45%" cy="45%" r="60%">
          <stop offset="0%" stop-color="var(--silver-light)"/>
          <stop offset="70%" stop-color="var(--silver-mid)"/>
          <stop offset="100%" stop-color="var(--silver-dark)"/>
        </radialGradient>
      </defs>
      <rect x="0" y="0" width="170" height="240" rx="80" fill="url(#silverTone)"/>
    </svg>

    <p class="tagline">An expression of love</p>
    <p class="occasion">THE PERFECT GIFT FOR YOUR LOVED ONE THIS MOTHER'S DAY</p>
    <p class="brand-name">VELORINE</p>
  </article>
</main>
</body>
</html>
```